Need eye catching book cover for book on Velmora Maidens

Book dimensions are 5.5 x 8.5; bright eye-catching cover for the title “Lanterns Still Burn Bright” about the Velmora Maidens and the Scrolls. A simple, clean aesthetic. Please do not use any original Maidens or the Velmora Tower. Designs depicting modern 2020 versions of the Maidens would be preferred with black/multicultural representation. Designs depicting crowns would also be preferred. This book is about determination, grit, 'living your best life - princess style'.

Target Market(s)

Young Adult

Industry/Entity Type

Christian

Font styles to use
Serif
Sans Serif
Decorative

Colors

Designer to choose colors to be used in the design.

Requirements
Must have
• Modern, clean, bright.

```html
<!DOCTYPE html>
<html lang="en">
<head>
<meta charset="utf-8">
<title>Lanterns Still Burn Bright — Cover Spread</title>
<link rel="stylesheet" href="https://fonts.googleapis.com/css2?family=Kaushan+Script&family=EB+Garamond&family=Cormorant+Garamond:wght@500&display=swap">
<style>
  :root {
    --page-bg: #eeeeef;
    --paper: #ffffff;
    --ink: #1d1d1d;
    --magenta: #c0144f;
    --plum: #7a2f6e;
    --slate: #4a5872;
    --teal: #1f8f87;
    --gown-light: #8fe3d0;
    --gown-mid: #6fb7d6;
    --gown-deep: #6a3fb0;
  }
  * { margin: 0; padding: 0; box-sizing: border-box; }
  html, body { width: 899px; height: 1200px; overflow: hidden; background: var(--page-bg); }
  .cover-spread {
    position: absolute; left: 20px; top: 302px; width: 859px; height: 595px;
    background: var(--paper);
    box-shadow: 0 2px 6px rgba(0,0,0,.25);
  }
  .back-blurb {
    position: absolute; left: 31px; top: 44px; width: 333px;
    font-family: "EB Garamond", serif; font-size: 9.6px; line-height: 12.1px;
    color: var(--ink); text-align: justify;
  }
  .back-blurb p + p { margin-top: 12px; }
  .crown-art { position: absolute; }
  .crown-art--back { left: 151px; top: 275px; width: 102px; height: 78px; }
  .crown-art--front { left: 754px; top: 130px; width: 51px; height: 35px; }
  .spine {
    position: absolute; left: 409px; top: 0; width: 40px; height: 595px;
  }
  .spine-title, .spine-author {
    position: absolute; left: 50%; white-space: nowrap;
    transform-origin: center; 
  }
  .spine-title {
    top: 200px; transform: translate(-50%, -50%) rotate(-90deg);
    font-family: "Kaushan Script", cursive; font-size: 26px; letter-spacing: 1px;
    background: linear-gradient(90deg, var(--teal), var(--plum) 55%, var(--magenta));
    -webkit-background-clip: text; background-clip: text; color: transparent;
  }
  .spine-author {
    top: 465px; transform: translate(-50%, -50%) rotate(-90deg);
    font-family: "Cormorant Garamond", serif; font-size: 13px; letter-spacing: 3px;
    color: var(--ink);
  }
  .front-title {
    position: absolute; left: 480px; top: 12px; width: 360px;
    font-family: "Kaushan Script", cursive; font-weight: 400;
  }
  .front-title span {
    display: block; line-height: 1;
    background: linear-gradient(180deg, var(--magenta) 0%, var(--plum) 40%, var(--slate) 65%, var(--teal) 100%);
    background-size: 100% 290px;
    -webkit-background-clip: text; background-clip: text; color: transparent;
  }
  .front-title .line-one { font-size: 76px; background-position: 0 0; }
  .front-title .line-two { font-size: 52px; margin-top: 6px; padding-left: 22px; background-position: 0 -100px; }
  .front-title .line-three { font-size: 70px; margin-top: -4px; padding-left: 6px; background-position: 0 -170px; }
  .figure-art {
    position: absolute; left: 676px; top: 168px; width: 150px; height: 372px;
  }
  .front-author {
    position: absolute; left: 514px; top: 553px; width: 300px; text-align: center;
    font-family: "Cormorant Garamond", serif; font-size: 23px; letter-spacing: 6px;
    color: var(--ink);
  }
</style>
</head>
<body>
  <section class="cover-spread">
    <div class="back-blurb">
      <p>Lorem ipsum dolor sit amet, consectetur adipiscing elit. Fusce eu arcu felis. Fusce vel congue lorem. Ut porta cursus pharetra. Aenean eget tellus urna. Donec venenatis eu lacus vitae luctus. Aliquam lobortis fringilla lorem vitae molestie. Nullam luctus eleifend magna id tincidunt. Phasellus ac lectus vitae urna placerat commodo id vel odio. Duis id lectus viverra, vulputate nisi sed, condimentum ipsum. Pellentesque sed semper ex.</p>
      <p>Donec non iaculis nulla. Nunc ac sem dolor. Donec eget lacus non lectus cursus aliquet. Nam quis dignissim erat, id tristique diam. Suspendisse finibus, massa eget dignissim bibendum, massa quam euismod orci, id auctor nisl erat a est. Phasellus malesuada mauris dui, et pellentesque nulla feugiat ut. Vivamus vitae porta elit. Pellentesque a risus fringilla, elementum eros sit amet, fringilla sapien. Aliquam lacinia nibh nibh. Proin urna neque, porttitor quis consequat vitae, accumsan id risus. Nunc id rhoncus nibh. Nunc at libero ac magna lacinia semper. Sed ac semper elit, lobortis sodales nibh.</p>
    </div>

    <svg class="crown-art crown-art--back" viewBox="0 0 102 78" role="img" aria-label="Hand-drawn crown doodle with sparkle lines">
      <rect x="0" y="0" width="102" height="78" fill="#f1f1f1"/>
    </svg>

    <div class="spine">
      <div class="spine-title">Lanterns Still Burn Bright</div>
      <div class="spine-author">AUTHOR NAME</div>
    </div>

    <h1 class="front-title">
      <span class="line-one">Lanterns</span>
      <span class="line-two">Still Burn</span>
      <span class="line-three">Bright</span>
    </h1>

    <svg class="crown-art crown-art--front" viewBox="0 0 51 35" role="img" aria-label="Small hand-drawn crown doodle">
      <rect x="0" y="0" width="51" height="35" fill="#f1f1f1"/>
    </svg>

    <svg class="figure-art" viewBox="0 0 150 372" role="img" aria-label="Painted illustration of a modern young princess in a flowing teal and violet ball gown">
      <defs>
        <linearGradient id="gownTone" x1="0" y1="0" x2="1" y2="1">
          <stop offset="0" stop-color="var(--gown-light)"/>
          <stop offset="0.55" stop-color="var(--gown-mid)"/>
          <stop offset="1" stop-color="var(--gown-deep)"/>
        </linearGradient>
      </defs>
      <rect x="0" y="0" width="150" height="372" rx="30" fill="url(#gownTone)" opacity="0.85"/>
    </svg>

    <div class="front-author">AUTHOR NAME</div>
  </section>
</body>
</html>
```